Our new beauty salon requires a price list brochure

Our beauty clinic is a medical grade skin care clinic. So our salon is very clinical and professional in appearance. I would like the colours to be similar to our logo design with some nice texture or abstract shapes thrown in.
Pricelist, contact details and logo is attached
I would prefer it to be a 3 fold brochure.

Target Market(s)

Females aged 30-50

Colors
85acd3
cedeed
c4c4c4
5c5c5c
000000
ffffff
eea3c7
f9d9e8
dbdbdb

Requirements
Must have
• easy to read

```html
<!DOCTYPE html>
<html lang="en">
<head>
<meta charset="utf-8">
<title>Willow Skin Clinic – Pricelist</title>
<link href="https://fonts.googleapis.com/css2?family=Allura&family=Manrope:wght@300;400;700;800&display=swap" rel="stylesheet">
<style>
  :root {
    --ink: #4d5b70;
    --ink-strong: #3f4d62;
    --panel-white: #ffffff;
    --panel-blue: #d3e2f0;
    --flower-dark: #5f6f86;
    --flower-mid: #8c9aae;
    --flower-light: #c4c9d2;
  }
  * { margin: 0; padding: 0; box-sizing: border-box; }
  html, body { width: 1200px; height: 927px; overflow: hidden; background: var(--panel-white); }
  body {
    font-family: "Manrope", Arial, sans-serif;
    font-weight: 300;
    color: var(--ink);
    font-size: 16.5px;
    line-height: 21.6px;
    letter-spacing: -0.3px;
  }
  .brochure { position: relative; width: 1200px; height: 927px; }
  .panel { position: absolute; top: 0; height: 927px; width: 400px; }
  .panel--left { left: 0; background: var(--panel-white); }
  .panel--middle { left: 400px; background: var(--panel-blue); }
  .panel--right { left: 800px; background: var(--panel-white); }

  .floral {
    position: absolute;
    border-radius: 50%;
    background: radial-gradient(ellipse at center, var(--flower-dark) 0%, var(--flower-mid) 35%, rgba(196,201,210,0.5) 60%, rgba(255,255,255,0) 72%);
    opacity: 0.8;
  }
  .floral--top-left { left: 190px; top: -80px; width: 270px; height: 290px; }
  .floral--bottom-left { left: -90px; top: 700px; width: 400px; height: 320px; }
  .floral--top-right { left: 770px; top: -120px; width: 380px; height: 250px; }
  .floral--bottom-right { left: 840px; top: 740px; width: 420px; height: 280px; }

  .title {
    position: absolute; left: 34px; top: 26px;
    font-family: "Allura", cursive;
    font-weight: 400;
    font-size: 58px; line-height: 70px;
    color: var(--ink-strong);
    letter-spacing: 0;
  }
  .price-group { position: absolute; text-align: center; }
  .price-group h2 {
    font-size: 16.5px; font-weight: 700; color: var(--ink-strong);
    letter-spacing: -0.4px;
  }
  .price-group h2 .note { font-weight: 300; }
  .inline-heading { font-weight: 700; color: var(--ink-strong); }
</style>
</head>
<body>
<main class="brochure">
  <section class="panel panel--left"></section>
  <section class="panel panel--middle"></section>
  <section class="panel panel--right"></section>

  <div class="floral floral--top-left" role="img" aria-label="Watercolour lily flower in slate blue and grey"></div>
  <div class="floral floral--bottom-left" role="img" aria-label="Watercolour lotus flower in slate blue"></div>
  <div class="floral floral--top-right" role="img" aria-label="Watercolour lilies in grey tones"></div>
  <div class="floral floral--bottom-right" role="img" aria-label="Watercolour lotus and lily bouquet in slate blue and grey"></div>

  <h1 class="title">Pricelist:</h1>

  <div class="price-group" style="left:24px; top:137px; width:180px;">
    <h2>IPL hair removal</h2>
    <p>Upper lip $50<br>Chin $50<br>Cheeks $75<br>Whole face $350</p>
  </div>
  <div class="price-group" style="left:24px; top:266px; width:180px;">
    <p>Bikini $90<br>G String $120<br>Brazilian $150</p>
  </div>
  <div class="price-group" style="left:24px; top:353px; width:180px;">
    <p>Underarms $90<br>Half arm $180<br>Full arm $250<br>Half leg $290<br>Thighs $290<br>Full leg $490</p>
  </div>
  <div class="price-group" style="left:24px; top:503px; width:180px;">
    <p>Full back $350<br>Shoulders $180<br>Nipples $60<br>Snail trail $50<br>Stomach $250<br>Chest $250<br>Buttocks $200</p>
  </div>

  <div class="price-group" style="left:175px; top:200px; width:210px;">
    <h2>IPL Photo Rejuvenation</h2>
    <p>Full face $350<br>Neck $200<br>Face, neck ad décolletage<br>$450<br>Spot Treatment $50</p>
  </div>
  <div class="price-group" style="left:175px; top:351px; width:210px;">
    <h2>Waxing</h2>
    <p>Eyebrow $21<br>Lip $15<br>Chin $15<br>Sides of face $20<br>Underarm $20<br>Forearm $25<br>Full arm $35<br>Lower leg $30<br>Upper leg $30<br>Full leg $50<br>Inner thigh $10<br>Snail trail $10<br>Bikini $30<br>G String $40<br>Brazilian $50<br>Eyebrow wax and Lip wax<br>$30<br>Eyebrow, lip and chin wax<br>$45</p>
  </div>

  <div class="price-group" style="left:420px; top:126px; width:360px;">
    <h2>Mens waxing</h2>
    <p>Mono brow $5<br>Eyebrow $21<br>Neck $20<br>Full back $45<br>Chest and Abdomen $45</p>
  </div>
  <div class="price-group" style="left:420px; top:277px; width:360px;">
    <h2>Tinting</h2>
    <p>Eyelash Tint $25<br>Lash Lift and Tint $80</p>
  </div>
  <div class="price-group" style="left:420px; top:362px; width:360px;">
    <p>Henna eyebrows and wax $80<br>Eyelash Tint and brow wax $40</p>
  </div>
  <div class="price-group" style="left:420px; top:428px; width:360px;">
    <p><span class="inline-heading">Willow Mini Facial</span>&nbsp; $80 &nbsp;40min</p>
  </div>
  <div class="price-group" style="left:420px; top:471px; width:360px;">
    <p><span class="inline-heading">Willow Deluxe Facial</span>&nbsp; $110 &nbsp;1 hour</p>
  </div>
  <div class="price-group" style="left:420px; top:515px; width:360px;">
    <p><span class="inline-heading">Microdermabrasion</span>&nbsp; $125</p>
  </div>
  <div class="price-group" style="left:420px; top:558px; width:360px;">
    <p><span class="inline-heading">Mini Micro</span> $80</p>
  </div>
  <div class="price-group" style="left:430px; top:601px; width:340px;">
    <h2>Wrinkle Relaxers</h2>
    <p>$175 per area (Crows, frown lines, forehead lines) or all 3 areas for $450<br>$50 minor areas (Gummy smile, brow lift, bunny lines)</p>
  </div>
  <div class="price-group" style="left:420px; top:730px; width:360px;">
    <p><span class="inline-heading">Dermal Fillers and Lip Fillers</span> $500 per ml</p>
  </div>

  <div class="price-group" style="left:830px; top:128px; width:350px;">
    <h2>Chemical Peels<br>Velora Peels</h2>
    <p>30min Lactic Acid Peels 20%/40%/60%<br>$120<br>Renewal Peel&nbsp; $120<br>Even Tone Peel $120<br>Clear Skin Peel&nbsp; $120</p>
  </div>
  <div class="price-group" style="left:830px; top:301px; width:350px;">
    <h2>Aurelle Peels <span class="note">&nbsp;30min</span></h2>
    <p>Berry Glow Peel $120<br>Red Fruit Peel $120<br>Balance Peel $120<br>Vitamin A Night Peel $250</p>
  </div>
  <div class="price-group" style="left:850px; top:452px; width:310px;">
    <h2>Solace LED</h2>
    <p>$90 per treatment &nbsp; or<br>$50 when added on to any of our other skin treatments.</p>
  </div>
  <div class="price-group" style="left:830px; top:559px; width:350px;">
    <h2>Serin Microneedling</h2>
    <p>(Collagen Induction Therapy)<br>$350 full face<br>$450 face, neck and décolletage</p>
  </div>
  <div class="price-group" style="left:830px; top:668px; width:350px;">
    <h2>Halcyon Laser Facial</h2>
    <p>$350 full face<br>$450 face, neck and décolletage</p>
  </div>
</main>
</body>
</html>
```